I am looking for a design that represent my gym/ performance facility that says respect the process on it. This images will be a center piece wall for my gym. I want this wall to stand out. This wall has to be clean and professional. This wall has to be Black and white. The gym is for athletes and regular members so the message has to relate to all. Respect the process represents this wall. Please be creative but clean and professional. Feel free to play with black and white body art. The message again should be "Respect The Process"
THE WALL IS 16FT LONG

Target Market(s)

Fitness and Athletes

Font styles to use
Sans Serif

Requirements
Must have
• Respect The Process
• Must all be in Black and white even images if you use them.
• Motivation words or phrases I.e., "Determination, Focus, Discipline,
• Please use famous or legendary athletes quotes.
• words to use:
• Transformation, Power, success, Strength, Commitment, Motivation, No Excuses, No Regrets, Never Give UP, Beast, Results, Dream Big, Consistency, Hard Work, Challenge,Warrior, Sacrifice, Greatness, Legendary, Winning, Zone, Purpose, Fight, Destiny,
• This Quote will stand alone:
• I HATED EVERY MINUTE OF TRAINING,
• BUT I SAID, "DON'T QUIT.
• SUFFER NOW AND LIVE THE REST
• OF YOUR LIFE A CHAMPION."
• -TOBIAS KERRIGAN
• "IF YOU DON'T WANT TO SACRIFICE FOR WHAT YOU WANT
• WHAT YOU WANT BECOMES THE SACRIFICE."
• "EVERYONE HAS THE DESIRE TO WIN, BUT ONLY CHAMPIONS HAVE THE DESIRE TO PREPARE."
• "IT'S ALWAYS SEEMS IMPOSSIBLE UNTIL IT'S DONE."
Nice to have
• It would be nice to have the words in Mustard yellow print as well as the white.T

```html
<!DOCTYPE html>
<html lang="en">
<head>
<meta charset="utf-8">
<title>Respect The Process – Gym Wall</title>
<link href="https://fonts.googleapis.com/css2?family=Righteous&family=Russo+One&family=Questrial&family=Arimo&display=swap" rel="stylesheet">
<style>
  :root {
    --paper: #ffffff;
    --ink: #0d0d0d;
    --mustard: #ffed1f;
    --white: #ffffff;
    --photo-black: #0c0c0c;
    --photo-dark: #222222;
    --photo-mid: #6e6e6e;
    --photo-light: #cfcfcf;
    --photo-peak: #e6e6e6;
  }
  html, body {
    margin: 0;
    padding: 0;
    overflow: hidden;
  }
  body {
    width: 915px;
    height: 1200px;
    background: var(--paper);
  }
  .poster {
    position: relative;
    width: 915px;
    height: 1200px;
    background: var(--paper);
    overflow: hidden;
  }
  .backdrop {
    position: absolute;
    left: 0;
    top: 0;
    width: 915px;
    height: 1126px;
    background: var(--ink);
  }
  .athlete-photo {
    position: absolute;
    left: 0;
    top: 103px;
    width: 915px;
    height: 995px;
    background:
      radial-gradient(ellipse 26% 20% at 47% 56%, var(--photo-peak) 0%, rgba(207,207,207,0.6) 45%, transparent 100%),
      radial-gradient(ellipse 22% 26% at 74% 74%, var(--photo-light) 0%, rgba(140,140,140,0.55) 55%, transparent 100%),
      radial-gradient(ellipse 20% 16% at 56% 28%, #b4b4b4 0%, rgba(110,110,110,0.5) 55%, transparent 100%),
      radial-gradient(ellipse 48% 55% at 64% 52%, var(--photo-mid) 0%, #3a3a3a 60%, transparent 95%),
      linear-gradient(90deg, #3a3a3a 0%, var(--photo-dark) 22%, var(--photo-black) 38%, #1a1a1a 70%, #2e2e2e 100%);
  }
  .title-block {
    position: absolute;
    left: 88px;
    top: 0;
    width: 211px;
    height: 207px;
    background: var(--mustard);
  }
  .title-block h1 {
    margin: 0;
    position: absolute;
    left: 37px;
    top: 57px;
    font-family: "Righteous", sans-serif;
    font-weight: 400;
    font-size: 31px;
    line-height: 46px;
    color: var(--ink);
    letter-spacing: -0.5px;
  }
  .headline-quote {
    position: absolute;
    left: 53px;
    top: 570px;
    margin: 0;
    font-family: "Righteous", sans-serif;
    font-weight: 400;
    font-size: 40px;
    line-height: 48px;
    color: var(--mustard);
    letter-spacing: -0.3px;
  }
  .prepare-quote {
    position: absolute;
    left: 53px;
    top: 748px;
    margin: 0;
    font-family: "Questrial", sans-serif;
    font-size: 14px;
    line-height: 18px;
    color: var(--white);
    letter-spacing: 0.6px;
  }
  .tagline-bar {
    position: absolute;
    left: 53px;
    top: 831px;
    width: 196px;
    height: 9px;
    background: var(--mustard);
    font-family: "Arimo", sans-serif;
    font-weight: 700;
    font-size: 5.5px;
    line-height: 9px;
    letter-spacing: 4px;
    color: var(--ink);
    padding-left: 6px;
    box-sizing: border-box;
    white-space: nowrap;
    overflow: hidden;
  }
  .effort-quote {
    position: absolute;
    left: 55px;
    top: 874px;
    margin: 0;
    font-family: "Russo One", sans-serif;
    font-style: italic;
    font-size: 23px;
    line-height: 29px;
    color: var(--mustard);
  }
  .values {
    position: absolute;
    left: 53px;
    top: 990px;
    margin: 0;
    padding: 0;
    list-style: none;
    font-family: "Arimo", sans-serif;
    font-size: 20px;
    line-height: 27px;
    color: var(--white);
  }
  .values .discipline { letter-spacing: 4.8px; }
  .values .focus { letter-spacing: 20px; }
</style>
</head>
<body>
  <main class="poster">
    <div class="backdrop"></div>
    <div class="athlete-photo" role="img" aria-label="Black and white photo of a muscular athlete curling a heavy dumbbell in a gym, barbell and weight plates behind him"></div>

    <div class="title-block">
      <h1>RESPECT<br>THE<br>PROCESS</h1>
    </div>

    <p class="headline-quote">I HATED EVERY MINUTE<br>OF TRAINING,<br>BUT I SAID, DON’T QUIT.</p>

    <p class="prepare-quote">EVERYONE HAS THE DESIRE TO WIN,<br>BUT ONLY CHAMPIONS HAVE THE DESIRE TO PREPARE.</p>

    <div class="tagline-bar">RESPECT THE PROCESS</div>

    <p class="effort-quote">ALWAYS MAKE a TOTAL EFFORT ,<br>EVEN WHEN the ODDS are<br>AGAINST&nbsp;&nbsp;&nbsp; YOU</p>

    <ul class="values">
      <li class="determination">Determination</li>
      <li class="discipline">Discipline</li>
      <li class="focus">Focus</li>
    </ul>
  </main>
</body>
</html>
```